Diet, Exercise, & Friends are Associated with Parkinson's disease Progression

We are researchers looking for modifiable variables associated with different rates of Parkinson's disease (PD) progression. This is a novel scale: www.VELKAM.org -- higher scores are associated with worse quality of life. Low is good. High is bad. Each of the dots is a real person (maybe those should disappear?). The line represents the typical rate of PD progression over time. Color scheme of different degrees of quality of life can change, but the general concept seems to be working. (see updated version at the bottom of the www.VELKAM.org website)We need to combine the exercise data from here. This poster was essentially my attempt at an infographic for scientists:https://files.exampledrop.net/static/7a21c4e9b0d3f5a6c8e1d2b4/t/8c33d1a7e5f2b9c4d6a1e7f3/2047719385210/TRV2017+Diet.pdf. The updated data is in the uploaded figure below. Please use this list/ verbage!I don't necessarily need to stick to red=bad, green=good, but that's the best I've been able to come up with to communicate all this. I can get the actual data output later, but it might be nice to be able to demonstrate intensity. Veggies are quite a bit better than spices. Loneliness is much, much worse than pasta. This is the original published data. We have updated data and want to turn it into an infographic (while we work on a new manuscript).https://www.quorvel.net/journals/jrbt/2017/8173920/
Target Market(s)
Individuals age 40-80 with Parkinson's disease (and their friends & family members).
Neurologists should be handing this out in their offices.
When patients ask their physician about nutrition, etc., we want this to be the 1-pg handout they give them.
Industry/Entity Type
Medicine
Font styles to use
Colors
Designer to choose colors to be used in the design.
Requirements
Must have
- VEL-KAM scale (www.VELKAM.org)-- use this picture on top. OK to change color.
- Lists foods/ activities associated with different rates of progression
- Title: "Food, Friends, and Exercise: Lifestyle Associations with PD Progression"
- Legend/ disclaimer (smaller font):
- "All results were adjusted for age, gender, and years since diagnosis. Total sample size: 1600+
- Based on the methods described in publication: "Effects of Meal Timing and Herbal Additives on Tremor Course" [Dunwarth RT et al, Jrnl Biol Tiss Rsch 2017], an updated analysis was performed on data on 7 May 2019. (N >1600)"
- "VEL-KAM scores available at www.VELKAM.org"
- Must fit on a single 8.5 x 11" page.
Nice to have
- The background should be white-- I want neurologists/ physicians downloading it, printing it, and distributing to patients. I don't want to waste ink.
- Logo for Wexmoor College and/or the logo for the "LUN Grove TR" Study. I like the WC emblem in one corner and the picture at the top of this website: www.VELKAM.org
- Would be nice if it could be understood between cultures and/ or easily translated.
- Would be nice if we could invite people to participate in the study!
- "To learn about joining the study, please to www.LUNGroveTR.wexmoor.edu"
Should not have
- Pictures of overweight people, or the impression that a muscular white guy is the ideal. I want to leave room for diversity and flexible interpretation.
- Too much text- a good-sized portion of this group will have poor vision and/or dementia. Needs to be simple.
- I like the simplicity of "Good" and "Bad"... don't love the labels. Seems to 'jugdgy'. Maybe "Encourage" and "Avoid" OR "Positive" and "Negative"

```html
<!DOCTYPE html>
<html lang="en">
<head>
<meta charset="utf-8">
<title>Food, Friends, and Exercise: Lifestyle Associations with PD Progression</title>
<link href="https://fonts.googleapis.com/css2?family=Source+Sans+3:wght@400;600;700&display=swap" rel="stylesheet">
<style>
  :root {
    --page: #f1eff0;
    --ink: #3b3a3c;
    --avoid-band: #fecba8;
    --avoid-box: #fea370;
    --avoid-shade: #c9875e;
    --encourage-band: #e0f4d8;
    --encourage-box: #c1e8ad;
    --encourage-shade: #8fa78a;
    --zone-poor: #fecaa6;
    --zone-fair: #fee4d6;
    --zone-good: #c8d4ec;
    --zone-excellent: #dff5d7;
  }
  * { margin: 0; padding: 0; box-sizing: border-box; }
  html, body { width: 928px; height: 1200px; overflow: hidden; }
  body {
    background: var(--page);
    color: var(--ink);
    font-family: "Source Sans 3", "Myriad Pro", sans-serif;
    position: relative;
  }
  .poster-title {
    position: absolute; left: 18px; width: 891px; top: 12px;
    text-align: center; font-weight: 700; font-size: 24px; line-height: 32px;
  }
  .band { position: absolute; left: 18px; width: 891px; }
  .band--avoid {
    top: 54px; height: 272px;
    background: linear-gradient(to bottom, var(--avoid-band) 0, var(--avoid-band) 92%, var(--avoid-shade) 100%);
  }
  .band--encourage {
    top: 722px; height: 340px;
    background: linear-gradient(to bottom, var(--encourage-shade) 0, var(--encourage-band) 6%, var(--encourage-band) 100%);
  }
  .panel { position: absolute; border-radius: 40px; }
  .panel--avoid { background: var(--avoid-box); top: 12px; height: 238px; width: 426px; }
  .panel--encourage { background: var(--encourage-box); top: 14px; height: 312px; width: 283px; }
  .panel__title {
    position: absolute; left: 0; right: 0; top: 14px; text-align: center;
    font-weight: 700; font-size: 21px; line-height: 28px;
  }
  .item {
    position: absolute; white-space: nowrap;
    font-size: 21px; line-height: 28px;
  }
  .chart { position: absolute; left: 0; top: 330px; }
  .chart text { font-family: "Source Sans 3", "Myriad Pro", sans-serif; fill: var(--ink); }
  .chart__title { font-size: 20px; font-weight: 700; }
  .chart__axis-title { font-size: 19px; font-weight: 700; }
  .chart__tick { font-size: 15px; }
  .chart__zone-label { font-size: 20px; }
  .legend {
    position: absolute; left: 30px; width: 868px; top: 1072px;
    font-size: 13px; line-height: 18px;
  }
  .legend p + p { margin-top: 3px; }
  .legend__link { font-weight: 600; }
</style>
</head>
<body>

  <h1 class="poster-title">Food, Friends, and Exercise: Lifestyle Associations with PD Progression</h1>

  <section class="band band--avoid">
    <div class="panel panel--avoid" style="left:11px;">
      <h2 class="panel__title">Foods to Avoid</h2>
      <span class="item" style="left:49px; top:58px;">Dairy</span>
      <span class="item" style="left:49px; top:86px;">Beef</span>
      <span class="item" style="left:49px; top:114px;">Chicken</span>
      <span class="item" style="left:49px; top:142px;">Fried Foods</span>
      <span class="item" style="left:49px; top:170px;">Soda</span>
      <span class="item" style="left:49px; top:198px;">Canned Fruits</span>
      <span class="item" style="left:193px; top:58px;">Canned Vegetables</span>
      <span class="item" style="left:193px; top:86px;">Frozen Vegetables</span>
    </div>
    <div class="panel panel--avoid" style="left:455px;">
      <h2 class="panel__title">Activities to Avoid</h2>
      <span class="item" style="left:43px; top:58px;">”I am overweight.”</span>
      <span class="item" style="left:45px; top:86px;">”I am lonely.”</span>
      <span class="item" style="left:45px; top:114px;">“I am Unhappy”</span>
      <span class="item" style="left:45px; top:142px;">“I don’t have lot of friends”</span>
      <span class="item" style="left:45px; top:170px;">“I eat too much”</span>
      <span class="item" style="left:45px; top:198px;">“I am in stress”</span>
    </div>
  </section>

  <svg class="chart" width="928" height="390" viewBox="0 0 928 390" role="img" aria-label="Line chart: VEL-KAM score rising with years since diagnosis across quality of life zones">
    <text class="chart__title" x="464" y="28" text-anchor="middle">Correlation Between Quality of Life and VEL-KAM Score</text>
    <rect x="146" y="48" width="702" height="108" fill="var(--zone-poor)"/>
    <rect x="146" y="156" width="702" height="54" fill="var(--zone-fair)"/>
    <rect x="146" y="210" width="702" height="54" fill="var(--zone-good)"/>
    <rect x="146" y="264" width="702" height="56" fill="var(--zone-excellent)"/>
    <text class="chart__zone-label" x="785" y="110" text-anchor="middle">Poor</text>
    <text class="chart__zone-label" x="786" y="190" text-anchor="middle">Fair</text>
    <text class="chart__zone-label" x="784" y="244" text-anchor="middle">Good</text>
    <text class="chart__zone-label" x="782" y="299" text-anchor="middle">Excellent</text>
    <line x1="146" y1="247" x2="735" y2="129" stroke="#222" stroke-width="1.3"/>
    <g stroke="#333" stroke-width="1.2" fill="none">
      <line x1="146" y1="40" x2="146" y2="320"/>
      <line x1="146" y1="320" x2="885" y2="320"/>
      <line x1="141" y1="48" x2="146" y2="48"/>
      <line x1="141" y1="102" x2="146" y2="102"/>
      <line x1="141" y1="156" x2="146" y2="156"/>
      <line x1="141" y1="210" x2="146" y2="210"/>
      <line x1="141" y1="264" x2="146" y2="264"/>
      <line x1="141" y1="318" x2="146" y2="318"/>
      <line x1="156" y1="320" x2="156" y2="326"/>
      <line x1="252" y1="320" x2="252" y2="326"/>
      <line x1="348" y1="320" x2="348" y2="326"/>
      <line x1="444" y1="320" x2="444" y2="326"/>
      <line x1="541" y1="320" x2="541" y2="326"/>
      <line x1="637" y1="320" x2="637" y2="326"/>
      <line x1="733" y1="320" x2="733" y2="326"/>
      <line x1="829" y1="320" x2="829" y2="326"/>
    </g>
    <g text-anchor="end">
      <text class="chart__tick" x="137" y="53">2500</text>
      <text class="chart__tick" x="137" y="107">2000</text>
      <text class="chart__tick" x="137" y="161">1500</text>
      <text class="chart__tick" x="137" y="215">1000</text>
      <text class="chart__tick" x="137" y="269">500</text>
      <text class="chart__tick" x="137" y="323">0</text>
    </g>
    <g text-anchor="middle">
      <text class="chart__tick" x="156" y="345">0</text>
      <text class="chart__tick" x="252" y="345">5</text>
      <text class="chart__tick" x="348" y="345">10</text>
      <text class="chart__tick" x="444" y="345">15</text>
      <text class="chart__tick" x="541" y="345">20</text>
      <text class="chart__tick" x="637" y="345">25</text>
      <text class="chart__tick" x="733" y="345">30</text>
      <text class="chart__tick" x="829" y="345">35</text>
    </g>
    <text class="chart__axis-title" x="464" y="380" text-anchor="middle">Years Since Diagnosis</text>
    <text class="chart__axis-title" transform="translate(68,182) rotate(-90)" text-anchor="middle">VEL-KAM Score</text>
    <text class="chart__axis-title" transform="translate(885,184) rotate(-90)" text-anchor="middle">Quality of Life</text>
  </svg>

  <section class="band band--encourage">
    <div class="panel panel--encourage" style="left:12px;">
      <h2 class="panel__title">Foods to Encourage</h2>
      <span class="item" style="left:44px; top:56px;">Fresh Vegetable</span>
      <span class="item" style="left:44px; top:84px;">Fresh Fruits</span>
      <span class="item" style="left:44px; top:112px;">Nuts &amp; Seeds</span>
      <span class="item" style="left:44px; top:140px;">Non-Fried Fish</span>
      <span class="item" style="left:44px; top:168px;">Olive &amp; Coconut Oil</span>
      <span class="item" style="left:44px; top:196px;">Fresh Herbs</span>
      <span class="item" style="left:44px; top:224px;">Spices</span>
      <span class="item" style="left:44px; top:252px;">Wine</span>
    </div>
    <div class="panel panel--encourage" style="left:306px;">
      <h2 class="panel__title">Activities to Encourage</h2>
      <span class="item" style="left:26px; top:60px;">”I try to eat organic</span>
      <span class="item" style="left:95px; top:87px;">when possible”</span>
      <span class="item" style="left:22px; top:128px;">”I have a lot of friends”</span>
      <span class="item" style="left:26px; top:168px;">”I cook most of my</span>
      <span class="item" style="left:126px; top:195px;">own meals"</span>
      <span class="item" style="left:26px; top:236px;">“I lost several pounds”</span>
    </div>
    <div class="panel panel--encourage" style="left:598px;">
      <h2 class="panel__title">Exercise to Encourage</h2>
      <span class="item" style="left:21px; top:56px;">7 days/ week of exercise</span>
      <span class="item" style="left:21px; top:82px;">is better than 6</span>
      <span class="item" style="left:21px; top:114px;">6 days/ week of exercise</span>
      <span class="item" style="left:21px; top:140px;">is better than 5…</span>
      <span class="item" style="left:21px; top:176px;">Trend continues to 3d/wk</span>
      <span class="item" style="left:21px; top:212px;">No benefit associated</span>
      <span class="item" style="left:21px; top:238px;">with 0-2 days/ wk</span>
    </div>
  </section>

  <footer class="legend">
    <p>All results were adjusted for age, gender, and years since diagnosis. Total sample size: 1600+</p>
    <p>Based on the methods described in publication: “Effects of Meal Timing and Herbal Additives on Tremor Course” [Dunwarth RT et al, Jrnl Biol Tiss Rsch 2017], an updated analysis was performed on data on 7 May 2019. (N &gt;1600)</p>
    <p>VEL-KAM scores available at <span class="legend__link">www.VELKAM.org</span></p>
    <p>To learn about joining the study, please go to <span class="legend__link">www.LUNGroveTR.wexmoor.edu</span></p>
  </footer>

</body>
</html>
```